Online Course Page

We are building a video based online course page. This project is for only the actual page that the student will watch the videos at. They will watch one vide at a time. Once one video lesson is completed then they can move to the next video lesson. The page will need to show the video player. (Main feature.) The list of lessons in the course. Instructor information. Profile picture and bio of the instructor. A Live chat button that will initiate a chat in real-time with the instructor.

The winning designer will also be asked to to design the dashboard area and other aspects of the user interface as an additional project.

Target Market(s)

Adults

Number of Pages Required

1 page

Colors
9bcb3c

Requirements
Must have
• Our logo is attached. Green and grey are our colors. Should feel modern, clean and be simple to navigate. The site will be responsive so the layout should work well on mobile devices.

```html
<!DOCTYPE html>
<html lang="en">
<head>
<meta charset="utf-8">
<title>LearnHarbor – Lesson 2</title>
<link href="https://fonts.googleapis.com/css2?family=Open+Sans:wght@400;600;700&display=swap" rel="stylesheet">
<style>
  :root {
    --green: #8dc449;
    --green-light: #c0e387;
    --green-dark: #3f6b1a;
    --ink: #111;
    --page: #f6f7f9;
    --grey: #a5a6aa;
    --grey-fade: #f7f7f8;
    --star: #d4c20a;
    --video: #000;
    --progress: #d7191b;
  }
  * { box-sizing: border-box; margin: 0; padding: 0; }
  html, body { width: 900px; height: 1200px; overflow: hidden; }
  body {
    position: relative;
    background: var(--page);
    font-family: "Open Sans", Arial, sans-serif;
    color: var(--ink);
  }
  .abs { position: absolute; }

  .top-strip { left: 0; top: 0; width: 900px; height: 16px; background: var(--green); }

  .brand { left: 56px; top: 47px; display: flex; align-items: center; gap: 8px; }
  .brand-dot { width: 26px; height: 26px; border-radius: 50%; background: var(--green); }
  .brand-name { font-size: 20px; font-weight: 700; color: var(--green); letter-spacing: -0.3px; }

  .main-nav { left: 0; top: 54px; width: 900px; font-size: 11.5px; font-weight: 600; }
  .main-nav a { position: absolute; color: var(--ink); text-decoration: none; white-space: nowrap; }
  .avatar { left: 812px; top: 39px; width: 42px; height: 42px; border-radius: 50%; background: var(--green); }

  .course-bar { left: 40px; top: 114px; width: 463px; height: 49px; background: var(--green);
    display: flex; align-items: center; padding-left: 13px; gap: 13px; font-size: 18px; }
  .course-bar .dot { width: 15px; height: 15px; border-radius: 50%; background: var(--ink); }

  .player { left: 40px; top: 165px; width: 463px; height: 281px; background: var(--video); color: #fff; }
  .player-title { position: absolute; left: 0; top: 100px; width: 100%; text-align: center; line-height: 21px; }
  .player-title strong { display: block; font-size: 16px; font-weight: 700; }
  .player-title span { font-size: 16px; }
  .player svg { position: absolute; left: 0; top: 0; }

  .lesson-heading { left: 40px; top: 476px; font-size: 20.5px; font-weight: 600; letter-spacing: -0.2px; }
  .rating { left: 331px; top: 515px; display: flex; align-items: center; gap: 8px; font-size: 11px; }

  .label { font-size: 12px; font-weight: 600; }
  .comments-label { left: 43px; top: 587px; }
  .comment-box { left: 40px; top: 618px; width: 461px; height: 102px; border: 1px solid #222; background: #fff; }
  .submit { left: 398px; top: 724px; width: 102px; height: 30px; background: #000; color: #fff;
    font-size: 13px; display: flex; align-items: center; justify-content: center; }

  .comment { left: 43px; width: 463px; font-size: 11.4px; line-height: 13.5px; }
  .comment p.author { margin-top: 14px; font-weight: 700; }

  .more { font-size: 11px; font-weight: 600; display: flex; align-items: center; gap: 2px; }

  .side-head { left: 528px; width: 334px; height: 49px; background: var(--green);
    display: flex; align-items: center; font-size: 12px; font-weight: 600; }
  .tabs span { position: absolute; top: 16px; }
  .tabs .active { color: #fff; }
  .tabs .active::after { content: ""; position: absolute; left: 22px; top: 18px;
    border: 4px solid transparent; border-top: 5px solid #fff; }

  .lesson-list { left: 528px; top: 165px; width: 334px; height: 417px;
    background: linear-gradient(#c2c3c5, var(--grey-fade)); }
  .lesson { position: absolute; left: 0; width: 334px; }
  .lesson .thumb, .related .thumb { position: absolute; width: 70px; height: 53px; background: #000; }
  .lesson .thumb { left: 40px; }
  .lesson .text { position: absolute; left: 126px; font-size: 11.5px; line-height: 20px; }
  .lesson .text b { font-weight: 700; }
  .lesson svg { position: absolute; left: 5px; }

  .related-list { left: 528px; top: 669px; width: 334px; height: 435px;
    background: linear-gradient(var(--grey), var(--grey-fade)); }
  .related { position: absolute; left: 0; width: 334px; height: 53px; }
  .related .text { position: absolute; left: 125px; top: 18px; font-size: 11.5px; }

  .footer { left: 0; top: 1160px; width: 900px; height: 40px; background: var(--green);
    display: flex; align-items: center; justify-content: center; font-size: 11.5px; }
</style>
</head>
<body>
  <div class="abs top-strip"></div>

  <div class="abs brand"><span class="brand-dot"></span><span class="brand-name">LearnHarbor</span></div>

  <nav class="abs main-nav">
    <a style="left:362px">HOME</a>
    <a style="left:440px">MY COURSES</a>
    <a style="left:544px">SUPPORT</a>
    <a style="left:638px">SETTINGS</a>
    <a style="left:733px">SIGN OUT</a>
  </nav>
  <svg class="abs avatar" viewBox="0 0 42 42" aria-label="Profile">
    <circle cx="21" cy="21" r="21" fill="var(--green)"/>
    <circle cx="21" cy="16" r="5.5" fill="#fff"/>
    <path d="M12 29c0-5 4-8 9-8s9 3 9 8z" fill="#fff"/>
  </svg>

  <div class="abs course-bar"><span class="dot"></span>COURSE NAME</div>

  <div class="abs player">
    <div class="player-title"><strong>LESSON 2</strong><span>Lorem ipsum dolor sit amet</span></div>
    <svg width="463" height="281" viewBox="0 0 463 281">
      <rect x="0" y="256" width="463" height="25" fill="#111"/>
      <rect x="0" y="256" width="463" height="5" fill="#555"/>
      <rect x="300" y="256" width="43" height="5" fill="#888"/>
      <rect x="0" y="256" width="300" height="5" fill="var(--progress)"/>
      <circle cx="300" cy="258.5" r="5" fill="#fff"/>
      <circle cx="300" cy="258.5" r="2" fill="var(--progress)"/>
      <rect x="289" y="233" width="22" height="13" rx="2" fill="#222"/>
      <text x="300" y="243" font-size="8" fill="#fff" text-anchor="middle" font-family="Open Sans, sans-serif" font-weight="700">2:45</text>
      <path d="M16 266v10l9-5z" fill="#aaa"/>
      <path d="M43 268h3l4-3v12l-4-3h-3z" fill="#aaa"/>
      <path d="M53 268q3 3 0 6M55 266q5 5 0 10" stroke="#aaa" fill="none"/>
      <text x="65" y="275" font-size="8" font-family="Open Sans, sans-serif" fill="#fff"><tspan font-weight="700">2:45</tspan><tspan fill="#aaa"> / 4:13</tspan></text>
      <path d="M339 267h10v6h-6l-3 3v-3h-1z" fill="#aaa"/>
      <circle cx="365" cy="271" r="4" fill="none" stroke="#aaa" stroke-width="2"/>
      <rect x="367" y="262" width="9" height="5" rx="1" fill="var(--progress)"/>
      <circle cx="387" cy="271" r="4" fill="#aaa"/>
      <rect x="403" y="268" width="10" height="6" fill="none" stroke="#aaa" stroke-width="1.5"/>
      <rect x="424" y="267" width="13" height="8" fill="none" stroke="#aaa" stroke-width="1.5"/>
      <path d="M445 269v-3h3M455 266h3v3M458 274v3h-3M448 277h-3v-3" stroke="#aaa" fill="none" stroke-width="1.5"/>
    </svg>
  </div>

  <h1 class="abs lesson-heading">LESSON 2 : HOW TO START YOUR COURSE</h1>
  <div class="abs rating">(107)
    <svg width="126" height="22" viewBox="0 0 126 22" aria-label="5 stars">
      <defs><path id="star" d="M11 1l3 7h7l-6 5 2 8-6-5-6 5 2-8-6-5h7z" fill="var(--star)"/></defs>
      <use href="#star" x="0"/><use href="#star" x="26"/><use href="#star" x="52"/><use href="#star" x="78"/><use href="#star" x="104"/>
    </svg>
  </div>

  <div class="abs label comments-label">COMMENTS</div>
  <div class="abs comment-box"></div>
  <div class="abs submit">Submit</div>

  <div class="abs comment" style="top:818px"><p>Lorem ipsum dolor sit amet, consectetuer adipiscing elit, sed diam nonummy nibh euis­mod tincidunt ut laoreet</p><p class="author">Mara L. on 22/10/2017</p></div>
  <div class="abs comment" style="top:905px"><p>Lorem ipsum dolor sit amet, consectetuer adipiscing elit, sed diam nonummy nibh euis­mod tincidunt ut laoreet</p><p class="author">Mara L. on 22/10/2017</p></div>
  <div class="abs comment" style="top:991px"><p>Lorem ipsum dolor sit amet, consectetuer adipiscing elit, sed diam nonummy nibh euis­mod tincidunt ut laoreet</p><p class="author">Mara L. on 22/10/2017</p></div>

  <div class="abs more" style="left:222px;top:1065px">LOAD MORE<svg width="10" height="8"><path d="M0 0h10l-5 8z"/></svg></div>

  <div class="abs side-head tabs" style="top:114px">
    <span class="active" style="left:17px">LESSONS</span>
    <span style="left:93px">INSTRUCTOR</span>
    <span style="left:202px">CHAT</span>
  </div>

  <div class="abs lesson-list">
    <div class="lesson" style="top:0;height:85px;background:#a6a7ab">
      <svg width="22" height="20" style="top:33px"><path d="M2 11l5 7 13-15" stroke="var(--green-dark)" stroke-width="3" fill="none"/></svg>
      <div class="thumb" style="top:16px"></div>
      <div class="text" style="top:21px"><b>LESSON 1</b><br>Lorem ipsum dolor sit amet</div>
    </div>
    <div class="lesson" style="top:85px;height:75px;background:var(--green-light)">
      <svg width="20" height="20" style="top:28px;left:8px"><path d="M0 2v16l16-8z" fill="#000"/></svg>
      <div class="thumb" style="top:11px"></div>
      <div class="text" style="top:16px"><b>LESSON 2</b><br>Lorem ipsum dolor sit amet</div>
    </div>
    <div class="lesson" style="top:171px;height:53px">
      <svg width="20" height="20" style="top:16px;left:8px"><path d="M0 2v16l16-8z" fill="#888"/></svg>
      <div class="thumb" style="top:0"></div>
      <div class="text" style="top:6px"><b>LESSON 3</b><br>Lorem ipsum dolor sit amet</div>
    </div>
    <div class="lesson" style="top:241px;height:53px">
      <svg width="20" height="20" style="top:16px;left:8px"><path d="M0 2v16l16-8z" fill="#888"/></svg>
      <div class="thumb" style="top:0"></div>
      <div class="text" style="top:6px"><b>LESSON 4</b><br>Lorem ipsum dolor sit amet</div>
    </div>
    <div class="lesson" style="top:318px;height:53px">
      <svg width="20" height="20" style="top:16px;left:6px"><path d="M0 2v16l16-8z" fill="#888"/></svg>
      <div class="thumb" style="top:0"></div>
      <div class="text" style="top:5px"><b>LESSON 5</b><br>Lorem ipsum dolor sit amet</div>
    </div>
    <div class="more" style="position:absolute;left:147px;top:389px">MORE <svg width="10" height="8"><path d="M0 0h10l-5 8z"/></svg></div>
  </div>

  <div class="abs side-head" style="top:618px;padding-left:17px">RELATED COURSES</div>

  <div class="abs related-list">
    <div class="related" style="top:22px"><div class="thumb" style="left:35px"></div><div class="text">Lorem ipsum dolor sit amet</div></div>
    <div class="related" style="top:100px"><div class="thumb" style="left:35px"></div><div class="text">Lorem ipsum dolor sit amet</div></div>
    <div class="related" style="top:178px"><div class="thumb" style="left:36px"></div><div class="text" style="left:126px">Lorem ipsum dolor sit amet</div></div>
    <div class="related" style="top:255px"><div class="thumb" style="left:37px"></div><div class="text" style="left:127px">Lorem ipsum dolor sit amet</div></div>
    <div class="related" style="top:333px"><div class="thumb" style="left:38px"></div><div class="text" style="left:128px">Lorem ipsum dolor sit amet</div></div>
    <div class="more" style="position:absolute;left:147px;top:396px">MORE <svg width="10" height="8"><path d="M0 0h10l-5 8z"/></svg></div>
  </div>

  <footer class="abs footer">Lorem ipsum dolor sit amet, consectetuer adipiscing</footer>
</body>
</html>
```